Housecleaning advertisement

We are a professional residential housecleaning service, in business since 2005, providing detailed, eco-friendly housecleaning to our clients. We are looking for a design that can be used in monthly coupon books ( 4c), quarterly local magazine (biz card sized 4c) and weekly newspaper ad (biz card sized b/w). We are looking for a retro feel - think 1940s kitchens - yellow, turquoise, bright red. we want to stress that we are a local firm, not a one-size fits all franchise. We provide very personalized service (linen changes, pet-friendly, flexible scheduling, sit down with customer prior to initial cleaning and discuss their priorities so that we know what they are looking for and deliver 110% each and every clean to them - and a a very reasonable price.) Our logo is a red car with two cleaners in it. Text for the ad :
Relax and enjoy your sparkling, clean, ready-for-company home!
Test drive our detailed, eco-friendly housecleaning
four hours for $100 (new clients only)
some bulleted points
* 100% Woman-owned and staffed. We know how to clean and tidy up - and treat your home with care and respect.
* Eco-friendly products - healthier for you and your family
* Fully insured and bonded.
415.382.9156
www.tidywrenhaus.net
Target Market(s)
Professional women ages 30-65 in the New Haven County, Ct market
Industry/Entity Type
Residential
Requirements
Nice to have
- retro 1940s 1950s

```html
<!DOCTYPE html>
<html lang="en">
<head>
<meta charset="utf-8">
<title>Tidy Wren Haus Housecleaning – Ad</title>
<link rel="stylesheet" href="https://fonts.googleapis.com/css2?family=Roboto+Condensed:wght@400;700&family=Oswald:wght@600&family=Roboto:wght@400;700&display=swap">
<style>
  :root {
    --sky-deep: #0f86c6;
    --sky: #1ea3dc;
    --sky-light: #5cc3ec;
    --bubble-center: #f4fbfe;
    --bubble-edge: #9fd9f3;
    --headline-cyan: #17a2df;
    --relax-pink: #e5177e;
    --phone-yellow: #fff27c;
    --white: #ffffff;
    --frame: #0b3550;
    --brand-red: #e2262c;
  }
  html, body {
    margin: 0;
    padding: 0;
    width: 1200px;
    height: 686px;
    overflow: hidden;
    background: #ffffff;
  }
  .ad {
    position: relative;
    width: 1200px;
    height: 686px;
    box-sizing: border-box;
    border: 3px solid var(--frame);
    background: linear-gradient(160deg, var(--sky-light) 0%, var(--sky) 45%, var(--sky-deep) 100%);
    overflow: hidden;
    color: var(--white);
  }
  .offer {
    position: absolute;
    left: 50px;
    top: 52px;
    width: 490px;
  }
  .offer__headline {
    margin: 0;
    font-family: "Roboto Condensed", sans-serif;
    font-weight: 700;
    font-size: 36px;
    line-height: 1.02;
    letter-spacing: -0.2px;
  }
  .offer__note {
    margin: 2px 0 0;
    font-family: "Roboto", sans-serif;
    font-weight: 400;
    font-size: 27px;
    line-height: 1;
  }
  .benefits {
    list-style: none;
    margin: 34px 0 0;
    padding: 0;
    font-family: "Roboto Condensed", sans-serif;
    font-weight: 400;
    font-size: 26px;
    line-height: 1.25;
  }
  .benefits__item {
    position: relative;
    padding-left: 22px;
    margin-bottom: 10px;
  }
  .benefits__item::before {
    content: "";
    position: absolute;
    left: 2px;
    top: 12px;
    width: 9px;
    height: 9px;
    border-radius: 50%;
    background: var(--white);
  }
  .benefits__item--star { padding-left: 0; }
  .benefits__item--star::before { display: none; }
  .divider {
    position: absolute;
    left: 51px;
    top: 486px;
    width: 430px;
    height: 0;
    border-top: 2px solid var(--white);
  }
  .contact__phone {
    position: absolute;
    left: 48px;
    top: 505px;
    margin: 0;
    font-family: "Roboto", sans-serif;
    font-weight: 700;
    font-size: 72px;
    letter-spacing: -1px;
    color: var(--phone-yellow);
    line-height: 1;
  }
  .contact__web {
    position: absolute;
    left: 51px;
    top: 582px;
    margin: 0;
    font-family: "Roboto", sans-serif;
    font-weight: 400;
    font-size: 44px;
    line-height: 1;
  }
  .bubble {
    position: absolute;
    left: 552px;
    top: 14px;
    width: 660px;
    height: 660px;
  }
  .message {
    position: absolute;
    left: 600px;
    top: 60px;
    width: 530px;
    margin: 0;
    text-align: center;
    font-family: "Oswald", sans-serif;
    font-weight: 600;
    text-transform: uppercase;
  }
  .message__relax {
    display: block;
    font-size: 74px;
    line-height: 1;
    color: var(--relax-pink);
  }
  .message__rest {
    display: block;
    font-size: 52px;
    line-height: 1.0;
    color: var(--headline-cyan);
  }
  .brand {
    position: absolute;
    left: 620px;
    top: 500px;
    width: 520px;
    display: flex;
    align-items: center;
    justify-content: center;
    gap: 14px;
    font-family: "Oswald", sans-serif;
    font-weight: 600;
    font-size: 34px;
    text-transform: uppercase;
    color: var(--brand-red);
  }
  .brand__dot {
    width: 26px;
    height: 26px;
    border-radius: 50%;
    background: var(--brand-red);
  }
</style>
</head>
<body>
<main class="ad">
  <section class="offer">
    <h1 class="offer__headline">Test drive our detailed,<br>eco-friendly housecleaning<br>four hours for $100</h1>
    <p class="offer__note">(new clients only)</p>
    <ul class="benefits">
      <li class="benefits__item">100% Woman-owned and staffed.<br>We know how to clean and tidy up - and<br>treat your home with care and respect.</li>
      <li class="benefits__item">Eco-friendly products - healthier<br>for you and your family</li>
      <li class="benefits__item benefits__item--star">* Fully insured and bonded.</li>
    </ul>
  </section>

  <div class="divider"></div>
  <p class="contact__phone">415.382.9156</p>
  <p class="contact__web">www.tidywrenhaus.net</p>

  <svg class="bubble" viewBox="0 0 660 660" aria-hidden="true">
    <defs>
      <radialGradient id="bubbleFill" cx="50%" cy="45%" r="55%">
        <stop offset="0%" stop-color="var(--bubble-center)"/>
        <stop offset="55%" stop-color="#d6effa"/>
        <stop offset="100%" stop-color="var(--bubble-edge)"/>
      </radialGradient>
    </defs>
    <circle cx="330" cy="330" r="328" fill="#8fd2f1"/>
    <circle cx="330" cy="330" r="318" fill="url(#bubbleFill)"/>
  </svg>

  <h2 class="message">
    <span class="message__relax">Relax</span>
    <span class="message__rest">And enjoy your<br>sparkling, clean,<br>ready-for-compa-<br>ny home!</span>
  </h2>

  <div class="brand">
    <span class="brand__dot"></span>
    <span class="brand__name">Tidy Wren Haus Housecleaning</span>
  </div>
</main>
</body>
</html>
```